Rosa Caring Star registered NDIS provider

Quality Care, Endless Support: Your NDIS Journey Starts Here
Rosa Caring Star is a compassionate Disability Support Service based in Liverpool NSW . We will provide you and your loved ones professional care and support that is tailored to your individual needs. We offer approved specialised short to long term disability accommodations, support independent living (SIL), assistance with daily tasks including cleaning, meal preparation and gardening, as well as daily programs and activities that range from personal training, community outings, videogames, table tennis, arts and craft, movies, and so much more!
To learn more about our services, feel free to browse our website to read about our NDIS-related blogs. For more information, get in touch with our friendly staff.
Work with Rosa Caring Star today. You and your loved ones deserve only the best.

ROSA CARING STAR
registered NDIS provider
Our services:
Approved specialised disability accommodations.

Support independent living SIL.

Short term accommodations/tenancy & respite.

Development of daily living & life skills

Overnight care active/non-active

Group/day centre activities

Assist in personal care.

Participation in community

Social and civic activities

Daily personal activities

Household tasks

Lawn mowing

Lifelong learning

Daily activities

Meal preparations

Support coordination

Plan management

Registered NDIS Provider
address 47 Brindle Crescent Liverpool NSW 2170
Phone : 0293416578/0471593824
Email : info@rosacaring.example.com.au
Web: : www.rosacaring.example.com.au
our servises in arabic
الخدمات تشمل
١- مساعدة التنقل .

٢- المشاركة الاجتماعية .

٣- تنمية المهارات الحياتية .

٤- مساعدة الأنشطة الشخصية .

٥- المساعدة في المهام المنزلية .

٦- مبيت (Respite ) وعناية على مدار ٢٤ ساعة .

٧- تطوير كافة المهارات اليومية مثلا تعلم الطبخ والميكاب تطوير المهارات الاجتماعية والحياة اليومية و طرق التنقل الامن مثل الباص و القطار
٨- العناية الشخصية والجسدية .
بإلاضافة الى السفرات الفردية والجماعية لمختلف الاعمار .

٩- بيوت مجهزة للسكن الدائمي لخدمات ذوي الاحتياجات الخاصه مع رعايه على مدار ٢٤ ساعة .

Target Market(s)

Disabilty people they need services from ndis provider which is my company registered company with ndis

Industry/Entity Type

Ndis disability services

Font styles to use
Serif

Colors
59FF00
82FF00
B8FF75
E3FFCB
F4FFEA
A7469A
B969AE
D3A5CF
EDDBEB
F8F0F9

Requirements
Must have
• Ndis logo and nice pictures for peoples with disability age from 9 years to 65 years
Should not have
• Old people

```html
<!DOCTYPE html>
<html lang="en">
<head>
<meta charset="utf-8">
<title>Rosa Caring Star – Our Services</title>
<link rel="stylesheet" href="https://fonts.googleapis.com/css2?family=Montserrat:wght@500;600;700&display=swap">
<style>
  :root {
    --stage: #d6d6d6;
    --paper: #ffffff;
    --purple-deep: #6c2170;
    --purple-mid: #8a338c;
    --purple-light: #a7469a;
    --green: #6cc83a;
    --ink: #1c1c1c;
    --white: #ffffff;
  }
  * { margin: 0; padding: 0; box-sizing: border-box; }
  html, body {
    width: 1200px;
    height: 1200px;
    overflow: hidden;
    background: var(--stage);
    font-family: "Montserrat", Arial, sans-serif;
  }
  .flyer {
    position: absolute;
    left: 230px;
    top: 76px;
    width: 740px;
    height: 1047px;
    overflow: hidden;
    background: linear-gradient(100deg, var(--purple-deep) 0%, var(--purple-mid) 55%, var(--purple-light) 100%);
  }
  .flyer-shapes {
    position: absolute;
    inset: 0;
    width: 740px;
    height: 1047px;
  }
  .brand-mark {
    position: absolute;
    left: 265px;
    top: 281px;
    width: 110px;
    height: 110px;
    border-radius: 50%;
    background: var(--green);
  }
  .brand-name {
    position: absolute;
    left: 495px;
    top: 304px;
    font-weight: 600;
    font-size: 38px;
    line-height: 41px;
    color: var(--ink);
  }
  .services-title {
    position: absolute;
    left: 44px;
    top: 412px;
    font-weight: 700;
    font-size: 50px;
    line-height: 60px;
    color: var(--white);
  }
  .services-list {
    position: absolute;
    left: 45px;
    top: 566px;
    list-style: none;
    color: var(--white);
    font-weight: 500;
    font-size: 15.5px;
    line-height: 25px;
  }
  .services-list li {
    position: relative;
    padding-left: 20px;
    white-space: nowrap;
  }
  .services-list li::before {
    content: "";
    position: absolute;
    left: 0;
    top: 8px;
    width: 9px;
    height: 9px;
    border: 1.5px solid var(--white);
    border-radius: 50%;
    opacity: 0.85;
  }
  .contact {
    position: absolute;
    right: 46px;
    top: 883px;
    text-align: right;
    color: var(--white);
    font-style: normal;
    font-weight: 500;
    font-size: 14.5px;
    line-height: 19px;
  }
  .contact-line {
    display: flex;
    justify-content: flex-end;
    align-items: center;
    gap: 8px;
    white-space: nowrap;
  }
  .contact-line.gap-before { margin-top: 19px; }
  .contact-icon {
    width: 11px;
    height: 11px;
    flex: none;
  }
  .contact-icon.blank { visibility: hidden; }
</style>
</head>
<body>
  <main class="flyer">
    <svg class="flyer-shapes" viewBox="0 0 592 838" preserveAspectRatio="none" aria-hidden="true">
      <path fill="var(--paper)" d="M0,0 L275,0 C170,20 45,105 0,229 Z"/>
      <path fill="var(--paper)" d="M276,0 L592,0 L592,349 C520,372 430,392 330,396 C260,399 200,390 160,362 C140,348 130,340 120,336 C85,330 60,315 56,285 C52,258 72,228 110,220 C92,200 92,165 108,140 C125,114 150,100 175,95 C182,60 215,25 276,0 Z"/>
    </svg>

    <div class="brand-mark" aria-hidden="true"></div>
    <h1 class="brand-name">ROSA<br>CARING<br>STAR</h1>

    <h2 class="services-title">Our<br>Services:</h2>

    <ul class="services-list">
      <li>Approved specialised disability accommodations.</li>
      <li>Support independent living SIL.</li>
      <li>Short term accommodations/tenancy &amp; respite.</li>
      <li>Development of daily living &amp; life skills</li>
      <li>Overnight care active/non-active</li>
      <li>Group/day centre activities</li>
      <li>Assist in personal care.</li>
      <li>Participation in community</li>
      <li>Social and civic activities</li>
      <li>Daily personal activities</li>
      <li>Household tasks</li>
      <li>Lawn mowing</li>
      <li>Lifelong learning</li>
      <li>Daily activities</li>
      <li>Meal preparations</li>
      <li>Support coordination</li>
      <li>Plan management</li>
    </ul>

    <address class="contact">
      <div class="contact-line">Registered NDIS Provider<svg class="contact-icon blank" viewBox="0 0 12 12"></svg></div>
      <div class="contact-line">47 Brindle Crescent Liverpool NSW 2170
        <svg class="contact-icon" viewBox="0 0 12 12" aria-hidden="true"><path fill="#fff" d="M6,0.5 C3.8,0.5 2.2,2.1 2.2,4.2 C2.2,7 6,11.5 6,11.5 C6,11.5 9.8,7 9.8,4.2 C9.8,2.1 8.2,0.5 6,0.5 Z M6,5.6 A1.4,1.4 0 1 1 6,2.8 A1.4,1.4 0 1 1 6,5.6 Z"/></svg>
      </div>
      <div class="contact-line gap-before">0293416578 / 0471593824
        <svg class="contact-icon" viewBox="0 0 12 12" aria-hidden="true"><path fill="#fff" d="M2.5,0.8 L4.3,0.8 L5.2,3.4 L3.9,4.4 C4.6,5.9 6.1,7.4 7.6,8.1 L8.6,6.8 L11.2,7.7 L11.2,9.5 C11.2,10.4 10.4,11.2 9.5,11.2 C4.8,11.2 0.8,7.2 0.8,2.5 C0.8,1.6 1.6,0.8 2.5,0.8 Z"/></svg>
      </div>
      <div class="contact-line">info@rosacaring.example.com.au
        <svg class="contact-icon" viewBox="0 0 12 12" aria-hidden="true"><rect x="0.8" y="2.5" width="10.4" height="7.5" rx="1" fill="#fff"/><path d="M1.2,3 L6,6.6 L10.8,3" fill="none" stroke="var(--purple-mid)" stroke-width="1"/></svg>
      </div>
      <div class="contact-line">www.rosacaring.example.com.au
        <svg class="contact-icon" viewBox="0 0 12 12" aria-hidden="true"><circle cx="6" cy="6" r="5.2" fill="none" stroke="#fff" stroke-width="1.2"/><ellipse cx="6" cy="6" rx="2.2" ry="5.2" fill="none" stroke="#fff" stroke-width="1"/><path d="M0.8,6 H11.2" stroke="#fff" stroke-width="1"/></svg>
      </div>
    </address>
  </main>
</body>
</html>
```